Meridian Cataract Surgery and Cosmetic Eyelid Surgery

We need Three page website design (home page and interior page template with two looks) with accompanying CSS code. 1. Home page, 2. General Eye-Care page, 3. Cosmetic Eyelid Surgery. #2 an #3 would be only slightly different. See below.

The site being redesigned is http://www.bright-lumen.com.

The content will remain consistent with the current site.

Additional graphics will be included, especially a number of "Before and after" photos of patients for the various procedures.

You can see competitive sites here: http://www.findoraq.com/search?q=cosmetic+eyelid+surgury+santa+rosa&ie=utf-8&oe=utf-8&aq=t&client=browser-b&rlz=1R1TTPP_en___US384

The client likes http://www.view-pmr.com, which has a serious look he likes (not necessarily the colors or design). Avoid too many "happy loving couples" and pretty women, on the main page or cataract/general eye-care pages. They are, however, good on the cosmetic pages.

When patients look at the *cosmetic surgery* pages, they can see the pretty women/couples. For *eye surgery* (which is what this is all about) they should see an attractive, active OLDER couple(s) on cataract surgery and refractive surgery pages.

In the US, premium IOL (Intraocular lens - a clear plastic lens that is implanted in the eye; usually done when the natural lens has been removed in a cataract operation) cataract surgery, cosmetic and refractive surgery are not fully paid for by insurance, so patients can afford to pay for it themselves and are more well-off than the normal market.
Updates

Do not use the graphics or look and feel of the current site.  We are looking for a NEW design, not a remix of the old elements.

The new logo is at http://www.artmarketo.com/file.aspx?fileLocation=claritonvisionlogo0.jpg

 
Do NOT use the old logo.  If your submitted design uses the old logo, please fix it and delete the one with the old logo.

Sorry for not making this clearer when we started.

Normal 0 false false false EN-US X-NONE X-NONE I want to see a home page that gives equal billing to general eyecare and cosmetic and RECONSTRUCTIVE eyelid surgery.   General eyecare should be listed first.  This should have the correct Practice name and Logo:   Meridian Sightcare and Cosmetic Eyelid Surgery Center.  The home page should be inviting to both old and young, men and women.  The General eyecare page should have similar appeal.  Cosmetic Page should be decidedly more feminine.  The home page should also highlight Dr. Brennick' s qualification and provide a site map/navigation.

The colors of the logo do not need to be limited to black and white.  The logos MUST be integrated into the design, not just pasted on the page.

Read the brief carefully and pay careful attention to the target markets.

 

vector art uploaded:  logo.ai

Target Market(s)

OLDER men and women. People whose faces, eyes, etc., have an aged look that they want to look younger. ALSO patients who want to have the best possible vision after CATARACT SURGERY. Patients who want Premium IOL'S which give them vision at both distance and near WITHOUT GLASSES. STATE OF THE ART GLAUCOMA SURGERY.

Industry/Entity Type

Plastic

Requirements
Must have
• Easy to read. Some readers may have vision difficulties. Easy to navigate for the elderly market. Cosmetic page may be a little more complex.

```html
<!DOCTYPE html>
<html lang="en">
<head>
<meta charset="utf-8">
<title>Cataract – Meridian Sightcare</title>
<link rel="stylesheet" href="https://fonts.googleapis.com/css2?family=PT+Sans&family=PT+Serif:ital,wght@0,400;0,700;1,400&display=swap">
<style>
:root{
  --night:#062a33;
  --night-band:#0d4550;
  --tab:#2b3a40;
  --sky:#1f9fd0;
  --link:#1a8ac2;
  --heading:#143a5c;
  --body:#555;
  --green:#74ad17;
  --muted:#888;
  --rule:#cfcfcf;
  --white:#fff;
  --diagram-a:#3a46c8;
  --diagram-b:#c8683a;
}
*{box-sizing:border-box;margin:0;padding:0}
html,body{width:1200px;height:1198px;overflow:hidden}
body{position:relative;font-family:"PT Serif",Georgia,serif;
  background:linear-gradient(var(--night) 0,var(--night) 471px,var(--night-band) 471px,var(--night-band) 487px,#d6d6d6 487px,#eeeeee 700px,#ececec 1115px,var(--night) 1115px)}
.abs{position:absolute}
a{text-decoration:none;color:inherit}
h1,h2{font-weight:400}

.brand{left:145px;top:30px;display:flex;align-items:center;gap:14px}
.brand-dot{width:44px;height:44px;border-radius:50%;background:var(--white)}
.brand-name{font-size:34px;color:var(--white);line-height:36px;letter-spacing:.5px}

.top-tab{left:639px;top:0;width:435px;height:47px;background:var(--tab);border-radius:0 0 6px 6px}
.top-link{top:13px;font-style:italic;font-size:16px;color:var(--white)}
.chev{font-style:normal;font-size:13px;margin-right:9px}

.call{right:205px;text-align:right;color:var(--sky);font-size:16px;line-height:19px}
.call b{font-weight:400;color:var(--white)}
.call1{top:66px;font-size:17px}
.call2{top:86px;font-size:15px}
.phone-icon{left:1008px;top:56px}

.mainnav{left:133px;top:126px;width:937px;height:73px;border-radius:8px;
  background:linear-gradient(#0b5c96,#1a94cf 55%,#2bb3e6)}
.nav-item{top:145px;color:var(--white);font-weight:700;font-size:16px;line-height:20px}
.nav-sep{top:148px;width:1px;height:36px;background:rgba(255,255,255,.35)}

.card{left:136px;top:210px;width:930px;height:885px;background:var(--white);border-radius:10px;box-shadow:0 1px 4px rgba(0,0,0,.15)}
.card-fade{left:136px;top:210px;width:220px;height:320px;border-radius:10px 0 0 0;background:linear-gradient(#e8e8e8,rgba(255,255,255,0))}

.side-title{left:164px;top:256px;font-weight:700;font-size:15px;line-height:17px;color:#7a7a7a}
.side-photo{left:166px;top:307px;width:162px;height:63px;border-radius:4px;background:linear-gradient(90deg,#d9c9bb,#b89886 50%,#e3d6cc)}
.side-divider{left:355px;top:305px;width:1px;height:695px;background:#e4e4e4}
.side-rule{left:166px;width:158px;border-top:1px dotted var(--rule)}
.side-link{left:170px;font-size:14px;color:var(--green)}
.side-link.current{color:var(--link)}
.side-link .chev{color:var(--link);font-size:12px;font-weight:700;margin-right:9px}

.promo{left:158px;top:744px;width:175px;height:158px;border:1px solid #e2e2e2;border-radius:8px;background:var(--white)}
.promo-img{left:164px;top:750px;width:163px;height:146px;border-radius:6px;background:linear-gradient(135deg,#a9cde0,#e9d8c6 60%,#cfe4ee)}
.promo-text{left:164px;top:838px;width:163px;text-align:center;color:var(--link);font-weight:700;font-size:22px;line-height:22px}
.promo-text span{display:block;font-size:27px;color:var(--heading)}
.promo-go{left:296px;top:869px;width:16px;height:16px;border-radius:50%;background:var(--sky)}

.title{left:378px;top:252px;font-size:26px;color:var(--link)}
.crumbs{left:379px;top:290px;font-size:11px;color:var(--muted)}
.crumbs b{color:#666}
.h2{left:379px;font-size:16px;color:var(--heading)}
.para{left:379px;width:650px;font-size:14px;line-height:16px;color:var(--body);letter-spacing:-.25px}
.list{left:380px;list-style:none;font-size:14px;line-height:22px;color:var(--link)}
.list li::before{content:"›";display:inline-block;width:21px;font-weight:700}

.shot{border-radius:2px}
.shot-clear{left:789px;top:435px;width:100px;height:85px;background:linear-gradient(#f4f4f4,#8c8c8c)}
.shot-fog{left:906px;top:435px;width:102px;height:85px;background:linear-gradient(#efefef,#bdbdbd)}
.caption{top:522px;width:110px;text-align:center;font-family:"PT Sans",Arial,sans-serif;font-size:12px;color:#222}
.diagram{top:893px;height:125px;background:linear-gradient(160deg,var(--diagram-a),var(--diagram-b))}

.foot-links{left:146px;top:1134px;font-family:"PT Sans",Arial,sans-serif;font-size:11px;color:#d6d6d6}
.foot-links span{margin:0 5px;color:#999}
.copy{left:146px;top:1157px;font-family:"PT Sans",Arial,sans-serif;font-size:11px;color:#999}
.address{right:190px;top:1134px;text-align:right;font-family:"PT Sans",Arial,sans-serif;font-size:10px;line-height:12px;color:#aaa}
.address b{color:#cfcfcf}
.social{left:1030px;top:1138px;width:22px;height:24px;border-radius:3px;background:#3b5fa8}
</style>
</head>
<body>

<header>
  <div class="abs brand"><span class="brand-dot"></span><span class="brand-name">Meridian Sightcare</span></div>

  <nav class="abs top-tab" aria-label="Utility"></nav>
  <a class="abs top-link" style="left:661px"><span class="chev">›</span>Main Page</a>
  <a class="abs top-link" style="left:781px"><span class="chev">›</span>Map to Our Office</a>
  <a class="abs top-link" style="left:951px"><span class="chev">›</span>Contact Us</a>

  <p class="abs call call1">Please call <b>(877) 555-0142</b></p>
  <p class="abs call call2">or <b>(707) 555-0186</b> for more information</p>
  <svg class="abs phone-icon" width="48" height="56" viewBox="0 0 48 56" aria-hidden="true">
    <g transform="rotate(-25 24 28)">
      <rect x="13" y="3" width="22" height="50" rx="4" fill="#3a4a50" stroke="#8a9aa0"/>
      <rect x="16" y="9" width="16" height="14" fill="#5a6a70"/>
      <g fill="#9aaab0"><circle cx="19" cy="29" r="1.5"/><circle cx="24" cy="29" r="1.5"/><circle cx="29" cy="29" r="1.5"/><circle cx="19" cy="35" r="1.5"/><circle cx="24" cy="35" r="1.5"/><circle cx="29" cy="35" r="1.5"/><circle cx="19" cy="41" r="1.5"/><circle cx="24" cy="41" r="1.5"/><circle cx="29" cy="41" r="1.5"/></g>
    </g>
  </svg>

  <nav class="abs mainnav" aria-label="Main"></nav>
  <a class="abs nav-item" style="left:176px">Cosmetic<br>Eyelid Surgery</a>
  <span class="abs nav-sep" style="left:320px"></span>
  <a class="abs nav-item" style="left:346px">How Aesthetic Eyelid<br>Surgery is Performed</a>
  <span class="abs nav-sep" style="left:541px"></span>
  <a class="abs nav-item" style="left:578px">Patient<br>Photos</a>
  <span class="abs nav-sep" style="left:672px"></span>
  <a class="abs nav-item" style="left:705px">General<br>Ophthalmology</a>
  <span class="abs nav-sep" style="left:854px"></span>
  <a class="abs nav-item" style="left:892px">About<br>Dr. Daniel Brennick</a>
</header>

<div class="abs card"></div>
<div class="abs card-fade"></div>

<aside>
  <p class="abs side-title">General<br>Ophthalmology</p>
  <div class="abs side-photo" role="img" aria-label="Portrait of a mature man"></div>
  <div class="abs side-divider"></div>
  <div class="abs side-rule" style="top:399px"></div>
  <a class="abs side-link current" style="top:414px"><span class="chev">›</span>Cataracts</a>
  <div class="abs side-rule" style="top:449px"></div>
  <a class="abs side-link" style="top:465px"><span class="chev">›</span>Diabetic Retinopathy</a>
  <div class="abs side-rule" style="top:499px"></div>
  <a class="abs side-link" style="top:516px"><span class="chev">›</span>Flashes and Floaters</a>
  <div class="abs side-rule" style="top:549px"></div>
  <a class="abs side-link" style="top:567px"><span class="chev">›</span>Glaucoma</a>
  <div class="abs side-rule" style="top:599px"></div>
  <a class="abs side-link" style="top:618px"><span class="chev">›</span>Macular Degeneration</a>
  <div class="abs side-rule" style="top:650px"></div>
  <a class="abs side-link" style="top:669px"><span class="chev">›</span>Refractive Surgery</a>
  <div class="abs side-rule" style="top:701px"></div>

  <div class="abs promo"></div>
  <div class="abs promo-img" role="img" aria-label="Smiling older couple at the seaside"></div>
  <p class="abs promo-text">Before&amp;After<span>Photos</span></p>
  <span class="abs promo-go"></span>
</aside>

<main>
  <h1 class="abs title">Cataract</h1>
  <p class="abs crumbs">Main Page &gt; General Pphthalmology &gt; <b>Cataracts</b></p>

  <h2 class="abs h2" style="top:330px">What is a cataract?</h2>
  <p class="abs para" style="top:366px">A cataract is a clouding of the normally clear lens of the eye. It can be compared to a window that is frosted or "fogged" with steam. There are many misconceptions about cataract. It is:</p>
  <ul class="abs list" style="top:418px">
    <li>Not a film over the eye;</li>
    <li>Not caused by overusing the eyes;</li>
    <li>Not a cancer;</li>
    <li>Not spread from one eye to the other;</li>
    <li>Not a cause of irreversible blindness.</li>
  </ul>
  <div class="abs shot shot-clear" role="img" aria-label="City skyline and road sign seen clearly"></div>
  <div class="abs shot shot-fog" role="img" aria-label="Same skyline seen through cataract haze"></div>
  <p class="abs caption" style="left:780px">Clear Sight</p>
  <p class="abs caption" style="left:899px">Cataract Vision</p>

  <h2 class="abs h2" style="top:543px">Common symptoms of cataract include:</h2>
  <ul class="abs list" style="top:581px">
    <li>A painless blurring of vision;</li>
    <li>Glare, or light sensitivity;</li>
    <li>Frequent eyeglass prescription changes;</li>
    <li>Double vision in one eye;</li>
    <li>Needing brighter light to read;</li>
    <li>Poor night vision;</li>
    <li>Fading or yellowing of colors.</li>
  </ul>
  <p class="abs para" style="top:750px">The amount and pattern of cloudiness within the lens can vary. If the cloudiness is not near the center of the lens, you may not be aware that a cataract is present.</p>

  <h2 class="abs h2" style="top:803px">What causes cataract?</h2>
  <p class="abs para" style="top:838px">The most common type of cataract is related to aging of the eye. Other causes of cataract include:</p>
  <ul class="abs list" style="top:874px">
    <li>Family history;</li>
    <li>Medical problems, such as diabetes;</li>
    <li>Injury to the eye;</li>
    <li>Medications, such as steroids;</li>
    <li>Long-term, unprotected exposure to sunlight;</li>
    <li>Previous eye surgery.</li>
  </ul>
  <div class="abs diagram" style="left:737px;width:132px" role="img" aria-label="Eye cross-section diagram labelled clear lens"></div>
  <div class="abs diagram" style="left:874px;width:150px" role="img" aria-label="Eye cross-section diagram labelled cataract"></div>
</main>

<footer>
  <p class="abs foot-links">Main Page<span>|</span>Site Map<span>|</span>Privacy Policy<span>|</span>Contact Us</p>
  <p class="abs copy">Copyright © 2011 Meridian Sightcare and Cosmetic Eyelid Surgery Center</p>
  <p class="abs address"><b>Daniel R. Brennick M.D.</b> 412 Alder Street<br>Millbrook, CA 95012<br>707-555-0186</p>
  <span class="abs social" aria-label="Social page"></span>
</footer>

</body>
</html>
```